Poster Design Project

About Us
Brimco is a company that specializes in providing communication solutions to the travel market. Our simple vision of “every hotel should have a mobile phone in the guest rooms”, led us to develop a path breaking cost effective mobile phone. With full integration capabilities with the hotels property management system, location based marketing, user locator and other features, this product is unique in addressing the hospitality segment.
Product Placement
The Brimco mobile will be placed in the hotel room on an A4 Sized transparent stand (the transparent stand is attached for your reference. If you notice, the phone will be placed in the jacket on the bottom left and in another jacket on the bottom right will be the brochure. So effectively, the design space available on the A4 brochure is only 60% of the space). The designed poster that we wish designed will be inserted in the A4 sized acrylic stand. The stand would typically be on the bedside table or on the study table of the hotel room. The A4 design should be bright and vibrant in keeping with our logo colors.
Attached is our logo. Also attached is the symbol of our phone that could be used innovatively on the brochure if you think it helps.
Attached is the content for the poster.
Reason: Feedback from the management team got delayed, hence the extension. Thanks
Reason: The delay is in the content finalization.

```html
<!DOCTYPE html>
<html lang="en">
<head>
<meta charset="utf-8">
<title>Brimco – In-room Phone Poster</title>
<link rel="stylesheet" href="https://fonts.googleapis.com/css2?family=Anton&family=Roboto+Condensed:wght@700&family=Open+Sans:wght@700&display=swap">
<style>
  :root {
    --field-green: #27cc0c;
    --field-light: #a8f25a;
    --band-cyan: #13e4f2;
    --band-blue: #1546e0;
    --band-yellow: #f7d92a;
    --band-orange: #ff4a10;
    --band-pink: #e63cc8;
    --band-crimson: #9a0418;
    --band-violet: #c064f0;
    --band-indigo: #4a12d8;
    --headline: #f5f51a;
    --plus-green: #3ed42a;
    --price-red: #f5000a;
    --price-shadow: #1a2be0;
    --ink-white: #ffffff;
    --strip-black: #000000;
    --bubble-dark: #2a2a2a;
    --bubble-edge: #9a9a9a;
    --badge-orange: #f7941d;
  }
  html, body {
    margin: 0;
    padding: 0;
    overflow: hidden;
    background: var(--field-green);
  }
  .poster {
    position: relative;
    width: 849px;
    height: 1200px;
    overflow: hidden;
  }
  .poster-art {
    display: block;
    width: 849px;
    height: 1200px;
  }
  .headline {
    font-family: "Anton", "Impact", sans-serif;
    fill: var(--headline);
  }
  .price {
    font-family: "Anton", "Impact", sans-serif;
    fill: var(--ink-white);
  }
  .brand-name, .tagline {
    font-family: "Roboto Condensed", "Arial Narrow", sans-serif;
    font-weight: 700;
    fill: var(--headline);
  }
  .badge-name {
    font-family: "Roboto Condensed", "Arial Narrow", sans-serif;
    font-weight: 700;
    fill: var(--strip-black);
  }
  .bubble-text {
    font-family: "Open Sans", "Arial", sans-serif;
    font-weight: 700;
    font-size: 14.5px;
    fill: var(--ink-white);
  }
</style>
</head>
<body>
<main class="poster">
  <svg class="poster-art" viewBox="0 0 849 1200" xmlns="http://www.w3.org/2000/svg">
    <defs>
      <radialGradient id="field-glow" cx="0.78" cy="0.55" r="0.55">
        <stop offset="0" stop-color="var(--field-light)"/>
        <stop offset="1" stop-color="var(--field-green)"/>
      </radialGradient>
      <linearGradient id="band-roaming" x1="0" y1="0" x2="1" y2="0">
        <stop offset="0" stop-color="var(--band-cyan)"/>
        <stop offset="0.45" stop-color="var(--band-blue)"/>
        <stop offset="1" stop-color="var(--band-blue)"/>
      </linearGradient>
      <linearGradient id="band-local" x1="0" y1="0" x2="1" y2="0">
        <stop offset="0" stop-color="var(--band-yellow)"/>
        <stop offset="0.35" stop-color="var(--band-orange)"/>
        <stop offset="1" stop-color="var(--band-orange)"/>
      </linearGradient>
      <linearGradient id="band-intl" x1="0" y1="0" x2="1" y2="0">
        <stop offset="0" stop-color="var(--band-pink)"/>
        <stop offset="0.7" stop-color="var(--band-crimson)"/>
        <stop offset="1" stop-color="#c0101e"/>
      </linearGradient>
      <linearGradient id="band-localcalls" x1="0" y1="0" x2="1" y2="0">
        <stop offset="0" stop-color="var(--band-violet)"/>
        <stop offset="0.6" stop-color="var(--band-indigo)"/>
        <stop offset="1" stop-color="var(--band-indigo)"/>
      </linearGradient>
      <linearGradient id="chevron-fade" x1="0" y1="0" x2="1" y2="0">
        <stop offset="0" stop-color="#2a2a2a"/>
        <stop offset="1" stop-color="#6a6a6a"/>
      </linearGradient>
    </defs>

    <!-- background field -->
    <rect class="field" width="849" height="1200" fill="url(#field-glow)"/>

    <!-- offer bands -->
    <path class="band band--roaming" fill="url(#band-roaming)"
          d="M0,0 L120,0 C350,80 600,210 849,235 L849,300 C600,300 300,240 0,150 Z"/>
    <path class="band band--local" fill="url(#band-local)"
          d="M0,150 C300,240 600,300 849,300 L849,395 C600,400 300,370 0,330 Z"/>
    <path class="band band--intl" fill="url(#band-intl)"
          d="M0,330 C300,370 600,400 849,395 L849,490 C600,530 300,530 0,500 Z"/>
    <path class="band band--localcalls" fill="url(#band-localcalls)"
          d="M0,500 C300,530 600,530 849,490 L849,585 C600,660 300,690 0,675 Z"/>

    <!-- brand badge -->
    <g class="brand-badge">
      <circle cx="695" cy="100" r="92" fill="var(--badge-orange)"/>
      <text class="badge-name" x="695" y="114" font-size="40" text-anchor="middle">Brimco</text>
    </g>

    <!-- offer lines -->
    <text class="headline offer-roaming" x="160" y="215" transform="rotate(8 160 215)"
          textLength="650" lengthAdjust="spacingAndGlyphs">
      <tspan font-size="36">SAVE </tspan><tspan font-size="72">80%</tspan><tspan font-size="42"> on international roaming</tspan>
    </text>

    <g class="plus" fill="var(--plus-green)">
      <rect x="323" y="305" width="24" height="86"/>
      <rect x="292" y="336" width="86" height="24"/>
    </g>
    <text class="headline offer-number" x="405" y="390" transform="rotate(-3 405 390)"
          textLength="400" lengthAdjust="spacingAndGlyphs">
      <tspan font-size="36">Get a </tspan><tspan font-size="58">LOCAL</tspan><tspan font-size="36"> number</tspan>
    </text>

    <g class="plus" fill="var(--plus-green)">
      <rect x="63" y="400" width="24" height="90"/>
      <rect x="30" y="433" width="90" height="24"/>
    </g>
    <text class="headline offer-intl" x="140" y="500" transform="rotate(-3.5 140 500)"
          textLength="680" lengthAdjust="spacingAndGlyphs">
      <tspan font-size="58">60 </tspan><tspan font-size="40">FREE minutes of international Calls</tspan>
    </text>

    <g class="plus" fill="var(--plus-green)">
      <rect x="193" y="555" width="24" height="90"/>
      <rect x="160" y="588" width="90" height="24"/>
    </g>
    <text class="headline offer-localcalls" x="285" y="630" transform="rotate(-7 285 630)"
          textLength="532" lengthAdjust="spacingAndGlyphs">
      <tspan font-size="62">60 </tspan><tspan font-size="40">FREE minutes of local calls</tspan>
    </text>

    <!-- price -->
    <g class="price-tag">
      <ellipse cx="222" cy="752" rx="200" ry="60" fill="var(--price-shadow)"/>
      <ellipse cx="210" cy="744" rx="200" ry="60" fill="var(--price-red)"/>
      <text class="price" x="200" y="772" font-size="76" text-anchor="middle">= 499 BHT</text>
    </g>

    <!-- brand strip -->
    <g class="brand-strip">
      <rect x="0" y="782" width="849" height="146" fill="var(--strip-black)"/>
      <g class="chevrons" fill="url(#chevron-fade)" opacity="0.75">
        <polygon points="250,790 285,790 340,855 285,920 250,920 305,855"/>
        <polygon points="290,790 325,790 380,855 325,920 290,920 345,855"/>
        <polygon points="330,790 365,790 420,855 365,920 330,920 385,855"/>
      </g>
      <text class="brand-name" x="16" y="858" font-size="34">Brimco</text>
      <text class="tagline" x="16" y="887" font-size="19">Pick up this phone NOW, to keep talking...</text>
    </g>

    <!-- feature bubbles -->
    <g class="feature-bubble">
      <polygon points="395,988 468,1022 392,1005" fill="var(--bubble-dark)" stroke="var(--bubble-edge)" stroke-width="2"/>
      <ellipse cx="327" cy="977" rx="80" ry="41" fill="var(--bubble-dark)" stroke="var(--bubble-edge)" stroke-width="2"/>
      <text class="bubble-text" x="284" y="974">Itemized bill</text>
      <text class="bubble-text" x="284" y="994">on checkout</text>
    </g>
    <g class="feature-bubble">
      <polygon points="380,1050 458,1062 378,1068" fill="var(--bubble-dark)" stroke="var(--bubble-edge)" stroke-width="2"/>
      <ellipse cx="312" cy="1052" rx="72" ry="39" fill="var(--bubble-dark)" stroke="var(--bubble-edge)" stroke-width="2"/>
      <text class="bubble-text" x="270" y="1046">Excellent call</text>
      <text class="bubble-text" x="270" y="1066">quality</text>
    </g>
    <g class="feature-bubble">
      <polygon points="358,1118 428,1116 355,1138" fill="var(--bubble-dark)" stroke="var(--bubble-edge)" stroke-width="2"/>
      <ellipse cx="292" cy="1124" rx="74" ry="40" fill="var(--bubble-dark)" stroke="var(--bubble-edge)" stroke-width="2"/>
      <text class="bubble-text" x="224" y="1112">Flexible tariff</text>
      <text class="bubble-text" x="224" y="1131">plans to choose</text>
      <text class="bubble-text" x="224" y="1150">from</text>
    </g>
  </svg>
</main>
</body>
</html>
```